Social-Business Application (iOS)

App is very simillar to "Murmel" from AppHarbor

Please see the wireframes!

We need a design for application according to attached wireframes.
Social-Business application is a mobile app, that let's user to login, using ProNexa and browse through other users content (meme's). There are 2 home pages and 4 categories (displayed in wireframes). They are pretty simillar to each other. First one is called "Say Something" and the other one called "Ask Something". On "Say Something" page user is able to browse through meme's with pictures. There are several options to each meme, as well as reply to meme with your own meme.
"Ask Something" has only 2 differences.
1. There are always "?" in the end of each meme.
2. Only plain background with different colors are acceptable.
User is also able to create meme's to each home page and category.

There is no First or Last name display! Only following info should be displayed:
Location, Industry, Number of ProNexa contacts.

There is also a simple chat function, that provides the ability to chat with author of the meme. On the chat preview we will show the meme preview Instead of profile picture.

Please, ask your questions.
Updates

Please, send your examples.

Please check out "Murmel" application for better understanding of the functionality and overall idea

https://apps.harborstore-example.com/store/apps/details?id=qz.murmel

I will report to our admin, to change Designer Payment to Commited if we will have at least one screen example from you, guys.

Target Market(s)

regular users, business users.
Adult Audience, Professional Audience.

Industry/Entity Type

Business

Font styles to use
Other font styles liked:
• Helvetica Neue

Requirements
Must have
• Design must have all screens and elements that are displayed in attached photos (wireframes).
Flat style is required.
Following the iOS guidelines is required.
Nice to have
• Design example could show different ui colors for each of home pages ("Ask Something" and "Say Something") to easily indicate on what home page user is.
Should not have
• The design should not be overloaded and should not use serif fonts like Times New Roman.

```html
<!DOCTYPE html>
<html lang="en">
<head>
<meta charset="utf-8">
<title>Latest – Social Business App</title>
<link rel="stylesheet" href="https://fonts.googleapis.com/css2?family=Ubuntu:wght@400;500;700&family=Oswald:wght@500&family=Special+Elite&display=swap">
<style>
  :root {
    --status-blue: #6cb1e8;
    --nav-blue: #82c1f0;
    --white: #ffffff;
    --page-bg: #ffffff;
    --edge-blue: #5aaeea;
    --edge-fade: #e6f2fb;
    --meta-text: #5f7284;
    --card-border: #dfe5ea;
    --footer-primary: #d5e8f8;
    --footer-secondary: #e9f3fb;
    --stat-text: #6b8296;
    --stat-icon: #4fb4dc;
    --dot-active: #a9d5f3;
    --dot-ring: #cfd3d7;
    --ask-button: #8a93a4;
  }
  * { box-sizing: border-box; margin: 0; padding: 0; }
  html, body { width: 676px; height: 1200px; overflow: hidden; background: var(--page-bg); }
  body { font-family: "Ubuntu", "Helvetica Neue", sans-serif; }
  .screen {
    position: relative; width: 640px; height: 1136px;
    transform: scale(1.05625); transform-origin: 0 0;
    background: var(--page-bg); overflow: hidden;
  }
  .status-bar {
    position: absolute; left: 0; top: 0; width: 640px; height: 40px;
    background: var(--status-blue); color: var(--white);
    font-family: "Helvetica Neue", "Ubuntu", sans-serif; font-size: 22px;
  }
  .status-bar span { position: absolute; top: 7px; }
  .status-carrier { left: 10px; }
  .status-time { left: 0; width: 640px; text-align: center; }
  .status-battery { right: 66px; }
  .status-bar svg { position: absolute; }
  .nav-bar {
    position: absolute; left: 0; top: 40px; width: 640px; height: 90px;
    background: var(--nav-blue);
  }
  .nav-title {
    position: absolute; left: 0; top: 26px; width: 640px; text-align: center;
    color: var(--white); font-size: 31px; font-weight: 700;
  }
  .nav-bar svg { position: absolute; }
  .badge {
    position: absolute; left: 582px; top: 14px; width: 28px; height: 28px; border-radius: 50%;
    background: var(--status-blue); border: 2px solid var(--white); color: var(--white);
    font-size: 13px; line-height: 24px; text-align: center;
  }
  .edge-strip {
    position: absolute; left: 0; top: 130px; width: 14px; height: 870px;
    background: linear-gradient(90deg, var(--edge-fade), var(--white));
  }
  .drawer-tab {
    position: absolute; left: 0; top: 556px; width: 47px; height: 50px;
    background: var(--edge-blue); border-radius: 0 25px 25px 0;
  }
  .drawer-tab svg { position: absolute; left: 7px; top: 11px; }
  .pager { position: absolute; top: 151px; left: 279px; display: flex; gap: 8px; }
  .pager-dot { width: 23px; height: 23px; border-radius: 50%; border: 2px solid var(--dot-ring); background: var(--white); }
  .pager-dot.active { background: var(--dot-active); border-color: var(--dot-active); }
  .post-card {
    position: absolute; width: 287px; height: 381px;
    border: 1px solid var(--card-border); background: var(--white);
  }
  .post-meta {
    height: 42px; line-height: 42px; text-align: center;
    color: var(--meta-text); font-size: 15px; font-weight: 500; white-space: pre;
  }
  .post-image {
    position: relative; height: 296px; overflow: hidden;
    display: flex; align-items: center; justify-content: center; text-align: center;
  }
  .post-caption {
    color: var(--white); font-family: "Oswald", "Ubuntu", sans-serif; font-size: 30px; line-height: 1.17;
    text-shadow: 0 0 4px rgba(0,0,0,.8), 1px 1px 2px #000; padding: 0 4px;
  }
  .caption-bottom { position: absolute; left: 0; right: 0; top: 228px; font-style: italic; font-size: 28px; }
  .caption-typed {
    position: absolute; left: 0; right: 0; top: 88px; text-align: left; padding-left: 2px;
    font-family: "Special Elite", "Courier New", monospace; color: #111; font-size: 25px; line-height: 1.5;
    text-shadow: 0 0 3px #fff, 0 0 3px #fff;
  }
  .post-stats { display: flex; height: 42px; }
  .stat {
    display: flex; align-items: center; justify-content: center; gap: 8px;
    color: var(--stat-text); font-size: 16px; font-weight: 500; background: var(--footer-secondary);
  }
  .stat-date { width: 122px; background: var(--footer-primary); }
  .stat-likes { width: 83px; }
  .stat-replies { width: 80px; }
  .ask-button {
    position: absolute; left: 35px; top: 1011px; width: 569px; height: 79px;
    background: var(--ask-button); border-radius: 4px; color: var(--white);
    font-size: 40px; font-weight: 500; text-align: center; line-height: 79px;
  }
</style>
</head>
<body>
<div class="screen">
  <header class="status-bar">
    <span class="status-carrier">●●●●○ Carrier</span>
    <span class="status-time">12:34 AM</span>
    <span class="status-battery">100%</span>
    <svg width="60" height="24" style="left:572px;top:8px" viewBox="0 0 60 24"><rect x="1" y="1" width="50" height="22" rx="4" fill="none" stroke="#fff" stroke-width="2"/><rect x="4" y="4" width="44" height="16" rx="2" fill="#fff"/><rect x="53" y="8" width="4" height="8" rx="1" fill="#fff"/></svg>
  </header>

  <nav class="nav-bar">
    <svg width="40" height="36" style="left:33px;top:27px" viewBox="0 0 40 36" fill="none" stroke="#fff" stroke-width="2.5"><rect x="2" y="2" width="15" height="14"/><rect x="22" y="2" width="15" height="14"/><rect x="2" y="20" width="15" height="14"/><rect x="22" y="20" width="15" height="14"/></svg>
    <h1 class="nav-title">Latest</h1>
    <svg width="42" height="30" style="left:551px;top:31px" viewBox="0 0 42 30" fill="none" stroke="#fff" stroke-width="2.5"><rect x="2" y="2" width="38" height="26"/><path d="M2 3 L21 18 L40 3 M2 27 L16 14 M40 27 L26 14"/></svg>
    <div class="badge">10</div>
  </nav>

  <div class="edge-strip"></div>
  <div class="drawer-tab"><svg width="28" height="28" viewBox="0 0 28 28" fill="none" stroke="#fff" stroke-width="2"><circle cx="14" cy="14" r="12"/><path d="M8 14 H19 M15 10 L19 14 L15 18"/></svg></div>

  <div class="pager"><span class="pager-dot"></span><span class="pager-dot active"></span><span class="pager-dot"></span></div>

  <article class="post-card" style="left:30px;top:195px">
    <div class="post-meta">Ukraine,  Information Tech, 546</div>
    <div class="post-image" role="img" aria-label="Photo of a couple embracing by a lake" style="background:linear-gradient(160deg,#9bb0bd 0%,#d9dedf 35%,#4a4645 60%,#8b6d52 100%)">
      <p class="post-caption caption-bottom">We met on Murmel,</p>
    </div>
    <div class="post-stats">
      <span class="stat stat-date"><svg width="22" height="22" viewBox="0 0 22 22" fill="none" stroke="var(--stat-icon)" stroke-width="2"><circle cx="11" cy="11" r="9"/><path d="M11 5v6h4"/></svg>25.4.2014</span>
      <span class="stat stat-likes"><svg width="24" height="22" viewBox="0 0 24 22" fill="none" stroke="var(--stat-icon)" stroke-width="2"><path d="M12 20 L3 11 A5 5 0 0 1 12 4 A5 5 0 0 1 21 11 Z"/></svg>324</span>
      <span class="stat stat-replies"><svg width="24" height="22" viewBox="0 0 24 22" fill="none" stroke="var(--stat-icon)" stroke-width="2"><path d="M3 10 C3 5 7 3 12 3 C17 3 21 5 21 10 C21 15 17 17 12 17 L6 20 L7 16 C4 15 3 13 3 10 Z"/></svg>226</span>
    </div>
  </article>

  <article class="post-card" style="left:338px;top:195px">
    <div class="post-meta">Ukraine,  Information Tech, 546</div>
    <div class="post-image" role="img" aria-label="Photo of a dorm room interior" style="background:linear-gradient(180deg,#3e3530 0%,#6a5648 45%,#8a6a4a 75%,#b09060 100%)">
      <p class="post-caption">Living in a dorm seriously sucks. It's like constantly being surround by self centered, disrespectful children.</p>
    </div>
    <div class="post-stats">
      <span class="stat stat-date"><svg width="22" height="22" viewBox="0 0 22 22" fill="none" stroke="var(--stat-icon)" stroke-width="2"><circle cx="11" cy="11" r="9"/><path d="M11 5v6h4"/></svg>25.4.2014</span>
      <span class="stat stat-likes"><svg width="24" height="22" viewBox="0 0 24 22" fill="none" stroke="var(--stat-icon)" stroke-width="2"><path d="M12 20 L3 11 A5 5 0 0 1 12 4 A5 5 0 0 1 21 11 Z"/></svg>324</span>
      <span class="stat stat-replies"><svg width="24" height="22" viewBox="0 0 24 22" fill="none" stroke="var(--stat-icon)" stroke-width="2"><path d="M3 10 C3 5 7 3 12 3 C17 3 21 5 21 10 C21 15 17 17 12 17 L6 20 L7 16 C4 15 3 13 3 10 Z"/></svg>226</span>
    </div>
  </article>

  <article class="post-card" style="left:30px;top:594px">
    <div class="post-meta">Ukraine,  Information Tech, 546</div>
    <div class="post-image" role="img" aria-label="Photo of a worried person holding their head" style="background:linear-gradient(180deg,#c9b8a6 0%,#a59080 40%,#3c3634 70%,#d8ccbf 100%)">
      <p class="caption-typed">WHAT'S YOUR BIGGEST FEAR ?  LET ME KNOW EVEN IF ITS PERSONAL I'M HERE TO LISTEN AND HELP! MINES IS LOVED ONES DYING :(</p>
    </div>
    <div class="post-stats">
      <span class="stat stat-date"><svg width="22" height="22" viewBox="0 0 22 22" fill="none" stroke="var(--stat-icon)" stroke-width="2"><circle cx="11" cy="11" r="9"/><path d="M11 5v6h4"/></svg>25.4.2014</span>
      <span class="stat stat-likes"><svg width="24" height="22" viewBox="0 0 24 22" fill="none" stroke="var(--stat-icon)" stroke-width="2"><path d="M12 20 L3 11 A5 5 0 0 1 12 4 A5 5 0 0 1 21 11 Z"/></svg>324</span>
      <span class="stat stat-replies"><svg width="24" height="22" viewBox="0 0 24 22" fill="none" stroke="var(--stat-icon)" stroke-width="2"><path d="M3 10 C3 5 7 3 12 3 C17 3 21 5 21 10 C21 15 17 17 12 17 L6 20 L7 16 C4 15 3 13 3 10 Z"/></svg>226</span>
    </div>
  </article>

  <article class="post-card" style="left:338px;top:594px">
    <div class="post-meta">Ukraine,  Information Tech, 546</div>
    <div class="post-image" role="img" aria-label="Photo of people shouting at someone" style="background:linear-gradient(90deg,#b98a6e 0%,#8a5e48 45%,#5a3a2c 75%,#3a2620 100%)">
      <p class="post-caption" style="margin-top:-96px">I'm deaf. it's not contagious. Stop acting like it is.</p>
    </div>
    <div class="post-stats">
      <span class="stat stat-date"><svg width="22" height="22" viewBox="0 0 22 22" fill="none" stroke="var(--stat-icon)" stroke-width="2"><circle cx="11" cy="11" r="9"/><path d="M11 5v6h4"/></svg>25.4.2014</span>
      <span class="stat stat-likes"><svg width="24" height="22" viewBox="0 0 24 22" fill="none" stroke="var(--stat-icon)" stroke-width="2"><path d="M12 20 L3 11 A5 5 0 0 1 12 4 A5 5 0 0 1 21 11 Z"/></svg>324</span>
      <span class="stat stat-replies"><svg width="24" height="22" viewBox="0 0 24 22" fill="none" stroke="var(--stat-icon)" stroke-width="2"><path d="M3 10 C3 5 7 3 12 3 C17 3 21 5 21 10 C21 15 17 17 12 17 L6 20 L7 16 C4 15 3 13 3 10 Z"/></svg>226</span>
    </div>
  </article>

  <div class="ask-button">Ask something?</div>
</div>
</body>
</html>
```